Mosquito and outdoor pest management

The uploaded logo must be integrated as the main theme of the card. I would like it to be modern and eye catching. Maybe some backround images or light silver metallic background.
Space enough at the base for contact info to be put in- phone numbers,emails,names,website.
Space on the back for short blog and lines for hand writing..calling card.
Target Market(s)
Commercial- golf courses, schools, outdoor function properties, pre event treatments.
Residential- retirement villages, townhome complexes and general houses
Industry/Entity Type
Management

```html
<!DOCTYPE html>
<html lang="en">
<head>
<meta charset="utf-8">
<title>Bayline Mosquito – Business Card</title>
<link rel="stylesheet" href="https://fonts.googleapis.com/css2?family=Cinzel:wght@400&family=Open+Sans:wght@400;600&display=swap">
<style>
  :root {
    --page: #e9e7e4;
    --black: #0c0c0c;
    --ink: #161616;
    --silver-hi: #f2f2f2;
    --silver-mid: #c9c9c9;
    --silver-lo: #9a9a9a;
    --red: #c8102e;
    --white: #ffffff;
    --grey: #9c9c9c;
    --rule: #b5b5b5;
  }
  * { box-sizing: border-box; margin: 0; padding: 0; }
  html, body { width: 1200px; height: 1023px; overflow: hidden; background: var(--page); }
  body { font-family: "Open Sans", sans-serif; position: relative; }

  .card {
    position: absolute;
    left: 290px;
    width: 620px;
    height: 354px;
    overflow: hidden;
    border-radius: 3px;
    box-shadow: 0 6px 18px rgba(0,0,0,.25);
  }
  .card--front { top: 110px; background: var(--black); }
  .card--back { top: 560px; background: var(--white); }

  /* front */
  .front-metal {
    position: absolute; inset: 0;
    background:
      repeating-linear-gradient(0deg, rgba(255,255,255,.08) 0 1px, rgba(0,0,0,.04) 1px 2px),
      linear-gradient(100deg, var(--silver-lo) 0%, var(--silver-hi) 38%, var(--silver-mid) 70%, var(--silver-hi) 100%);
  }
  .front-swoosh { position: absolute; inset: 0; width: 100%; height: 100%; }

  .brand {
    position: absolute;
    display: flex; align-items: center; gap: 12px;
  }
  .brand__mark { width: 14px; height: 14px; background: var(--red); flex: none; }
  .brand__name { font-family: "Open Sans", sans-serif; font-weight: 600; letter-spacing: .04em; text-transform: uppercase; }
  .brand--front { left: 60px; top: 74px; }
  .brand--front .brand__name { color: var(--ink); font-size: 30px; line-height: 1.15; }

  .contact { position: absolute; left: 34px; top: 220px; color: var(--white); }
  .contact__name { font-family: "Cinzel", serif; color: var(--red); font-size: 24px; letter-spacing: .04em; }
  .contact__role { font-size: 12px; margin: 2px 0 8px; }
  .contact__list { list-style: none; font-size: 13px; }
  .contact__list li { display: flex; align-items: center; gap: 8px; line-height: 22px; }
  .contact__icon { width: 13px; height: 13px; flex: none; }

  .address {
    position: absolute; right: 26px; top: 238px;
    text-align: right; color: var(--grey); font-size: 13px; line-height: 20px;
  }

  /* back */
  .back-band { position: absolute; left: 0; top: 0; width: 100%; height: 100%; }
  .brand--back { left: 34px; top: 30px; }
  .brand--back .brand__mark { width: 10px; height: 10px; }
  .brand--back .brand__name { color: var(--white); font-size: 17px; line-height: 1.2; }

  .writing-lines { position: absolute; left: 28px; right: 28px; top: 112px; list-style: none; }
  .writing-lines li { height: 20px; border-bottom: 1px dashed var(--rule); }
</style>
</head>
<body>

<section class="card card--front" aria-label="Business card front">
  <div class="front-metal"></div>
  <svg class="front-swoosh" viewBox="0 0 620 354" preserveAspectRatio="none" aria-hidden="true">
    <path d="M0 190 C 180 200, 420 205, 620 168 L620 354 L0 354 Z" fill="var(--black)"/>
    <path d="M40 196 C 220 206, 430 204, 600 172 C 430 198, 220 202, 40 196 Z" fill="var(--white)" opacity=".85"/>
  </svg>

  <div class="brand brand--front">
    <span class="brand__mark"></span>
    <span class="brand__name">Bayline Mosquito<br>and Outdoor Pest Management</span>
  </div>

  <div class="contact">
    <h1 class="contact__name">Marten Kovac</h1>
    <p class="contact__role">CEO &amp; Managing Director</p>
    <ul class="contact__list">
      <li>
        <svg class="contact__icon" viewBox="0 0 14 14"><rect width="14" height="14" rx="2" fill="var(--red)"/><path d="M4 3.5 L6 3.5 L6.6 5.6 L5.6 6.4 C6.2 7.6 7 8.4 8 9 L8.8 8 L10.5 8.6 L10.5 10.5 C7 10.5 4 7.5 4 3.5 Z" fill="var(--white)"/></svg>
        0400 555 218
      </li>
      <li>
        <svg class="contact__icon" viewBox="0 0 14 14"><rect width="14" height="14" rx="2" fill="var(--red)"/><rect x="3" y="4.5" width="8" height="5.5" fill="none" stroke="var(--white)" stroke-width="1"/><path d="M3 4.5 L7 7.5 L11 4.5" fill="none" stroke="var(--white)" stroke-width="1"/></svg>
        marten.kovac@baylinepest.com.au
      </li>
      <li>
        <svg class="contact__icon" viewBox="0 0 14 14"><rect width="14" height="14" rx="2" fill="var(--red)"/><circle cx="7" cy="7" r="3.8" fill="none" stroke="var(--white)" stroke-width="1"/><path d="M3.2 7 H10.8 M7 3.2 C5.4 5 5.4 9 7 10.8 M7 3.2 C8.6 5 8.6 9 7 10.8" fill="none" stroke="var(--white)" stroke-width=".8"/></svg>
        www.baylinepest.com.au
      </li>
    </ul>
  </div>

  <address class="address" style="font-style:normal">
    Level 12, 40 Harbour Lane<br>
    Sydney, NSW, 2000<br>
    Australia
  </address>
</section>

<section class="card card--back" aria-label="Business card back">
  <svg class="back-band" viewBox="0 0 620 354" preserveAspectRatio="none" aria-hidden="true">
    <path d="M0 0 H620 V86 C 430 104, 200 100, 0 92 Z" fill="var(--black)"/>
    <path d="M20 94 C 220 102, 430 104, 600 90 C 430 98, 220 98, 20 94 Z" fill="var(--white)" opacity=".9"/>
  </svg>

  <div class="brand brand--back">
    <span class="brand__mark"></span>
    <span class="brand__name">Bayline Mosquito<br>and Outdoor Pest Management</span>
  </div>

  <ul class="writing-lines" aria-label="Lines for handwritten notes">
    <li></li><li></li><li></li><li></li><li></li><li></li>
    <li></li><li></li><li></li><li></li><li></li>
  </ul>
</section>

</body>
</html>
```